Powerpoint design template for FLOMBIRT for new digital platform

We would like to use a PowerPoint template, we would like to create a new page, we would like to create a new digital platform FLOMBIRT for schools and parents for the creation of playful communication and educational tools for children to enhance their positive development, amaze them learn in a playful way. This platform is going to be the most creative, stimulating and innovative classroom, easy to use and fast to implement. Scrapbooking, collages ... Magazine, newsletters Diplomla / awards Slideshows Facebook Calendars Organizers Greetings Games ... This powerpoint template will be used essential to We are looking for a professional design, positioning our brand in the children market with an adult hearing. so you will need to find a good deal. Primary target: nurseries & schools from 0 to 18 years old and universities (in 2nd phase) Secondary target: small & medium businesses Third target: general public, and TPE If it is a color scheme, then it is suggested that it be marketed in Europe (UK, Italy, Spain) and in a 2nd Stage USA and other countries. multiple options for front page, insidious pages (multiple styles with limited text and extended text) and final contact page We need something to read, we can not do it too much, but we can not do it. , and inside pages aligned to our logo

Target Market(s)

Target 1; Education with teacher Target 2; parents and grandparents

Industry/Entity Type

Education

Font styles to use
Other font styles liked:
• not decided. but not too fancy

Requirements
Must have
• Multi page options for front page, page insides (multiple styles with limited text and extended text) and final page contact
Nice to have
• do not have a lot of ideas. We need something to read, we can not get away from it
Should not have
• not too fancy and busy: keep clarity & simplicity while reassuring on quality

```html
<!DOCTYPE html>
<html lang="en">
<head>
<meta charset="utf-8">
<title>Who we are – Flombirt</title>
<link rel="stylesheet" href="https://fonts.googleapis.com/css2?family=Open+Sans:ital,wght@0,400;0,700;1,400&display=swap">
<style>
  :root {
    --bg: #ffffff;
    --header-bg: #ffffff;
    --title: #6f6f6f;
    --body-text: #7a7a7a;
    --blue: #3db8ea;
    --pink: #e0458a;
    --orange: #ef9b36;
    --brand: #3a3a3a;
    --brand-mark: #c7df3a;
    --visual-pink: #f2b6dd;
    --visual-blue: #9fc6ea;
    --visual-cream: #f3ead2;
    --visual-green: #cfe3b0;
    --visual-silver: #cfcfd2;
  }
  html, body {
    margin: 0;
    padding: 0;
    overflow: hidden;
  }
  body {
    width: 1200px;
    height: 674px;
    background: var(--bg);
    font-family: "Open Sans", sans-serif;
  }
  .slide {
    position: relative;
    width: 1200px;
    height: 674px;
    overflow: hidden;
    background: var(--bg);
  }
  .header-band {
    position: absolute;
    left: 40px;
    top: 38px;
    width: 1160px;
    height: 62px;
    background: var(--header-bg);
    box-shadow: 0 3px 8px rgba(0,0,0,0.16);
  }
  .slide-title {
    position: absolute;
    left: 86px;
    top: 47px;
    margin: 0;
    font-style: italic;
    font-weight: 400;
    font-size: 34px;
    line-height: 46px;
    color: var(--title);
    letter-spacing: -0.5px;
  }
  .brand {
    position: absolute;
    left: 968px;
    top: 48px;
    display: flex;
    align-items: center;
    gap: 10px;
  }
  .brand-mark {
    width: 24px;
    height: 24px;
    background: var(--brand-mark);
  }
  .brand-name {
    font-weight: 700;
    font-size: 32px;
    line-height: 44px;
    color: var(--brand);
  }
  .points {
    position: absolute;
    left: 59px;
    top: 172px;
    width: 435px;
    margin: 0;
    padding: 0;
    list-style: none;
  }
  .point {
    position: relative;
    padding-left: 36px;
    margin-bottom: 19px;
    font-size: 25px;
    line-height: 31.7px;
    color: var(--body-text);
  }
  .point::before {
    content: "";
    position: absolute;
    left: 0;
    top: 6px;
    width: 20px;
    height: 20px;
  }
  .point--blue::before { background: var(--blue); }
  .point--pink::before { background: var(--pink); }
  .point--orange::before { background: var(--orange); }
  .platform-visual {
    position: absolute;
    left: 574px;
    top: 162px;
    width: 572px;
    height: 460px;
    border-radius: 12px;
    background:
      radial-gradient(circle at 22% 30%, var(--visual-pink) 0%, rgba(242,182,221,0) 38%),
      radial-gradient(circle at 78% 28%, var(--visual-blue) 0%, rgba(159,198,234,0) 40%),
      radial-gradient(circle at 55% 62%, var(--visual-green) 0%, rgba(207,227,176,0) 38%),
      radial-gradient(circle at 20% 75%, #e7b8f0 0%, rgba(231,184,240,0) 35%),
      linear-gradient(180deg, var(--visual-cream) 0%, #f4f1ea 70%, var(--visual-silver) 100%);
  }
</style>
</head>
<body>
  <main class="slide">
    <div class="header-band"></div>
    <h1 class="slide-title">Who we are…</h1>
    <div class="brand">
      <span class="brand-mark"></span>
      <span class="brand-name">FLOMBIRT</span>
    </div>

    <ul class="points">
      <li class="point point--blue">A new digital platform developed to provide stimulating, creative and playful educational tools for children of all ages</li>
      <li class="point point--pink">Designed to be easy and intuitive to use, Flombirt will provide a virtual classroom for children both in schools and at home</li>
      <li class="point point--orange">Flombirt will feature a wide range of content, including schoolbooks, tools for scrapbooking and collage, magazines, slideshows and games</li>
    </ul>

    <div class="platform-visual" role="img" aria-label="Desktop computer screen showing a colourful collage of educational content: books, scrapbooking pages, word games, a calendar and learning apps"></div>
  </main>
</body>
</html>
```